Hopscotch Nell needs updated Marketing Material!

Moving business to a new location and am looking to update all marketing material, including business cards, postcards, flyers, website. I've attached a copy of my current business card.
Updates

Good Morning!  I just received my new business phone number.  It is 583-402-9176

Hello All Designers!

Thank you for all the submissions I have received so far!  I wanted to give you a bit more background on what Hopscotch Nell is all about:

I started this service when I was downsized out of a sales and marketing position.   A friend asked if I had time to run a few errands for her while she was at work.  "Lightbulb"!  I thought there must be more people that are over worked, over booked and want nothing more to do when they get home than spend time with their families or just relaxing.  And who wants to do all their running around on the weekends??  Hopscotch Nell was born!

I have been extremely fortunate with my business here in California.  However, this summer I will be moving to a small town in Pennsylvania and I will be in uncharted territory.  I hope to have marketing material that will "WOW" all new potential clients.  Letting them know that I offer a unique service that can put time back into their week and free up their weekends for more important things.

If there is anything else I can tell you in order to help you with your design process, please let me know!
Thank you!
Nellie

Target Market(s)

Busy working parents and young professionals with disposable income that would like to spend their down time doing things that they enjoy rather than doing errands.

Industry/Entity Type

Marketing

```html
<!DOCTYPE html>
<html lang="en">
<head>
<meta charset="utf-8">
<title>Hopscotch Nell – Business Card</title>
<link rel="stylesheet" href="https://fonts.googleapis.com/css2?family=Crimson+Pro:wght@700&family=Varela+Round&display=swap">
<style>
  :root {
    --page: #ffffff;
    --card-grey: #a4a4a4;
    --band-green: #4cc23a;
    --band-green-soft: #6cc85c;
    --brand-red: #8e1b12;
    --ink-purple: #3b2f92;
    --ink-magenta: #d8157f;
    --ink-white: #ffffff;
    --item-blue: #2f2a9c;
    --item-red: #e2231a;
    --item-yellow: #f2d300;
    --item-green: #0c9a4f;
    --item-pink: #e0128a;
    --serif: "Crimson Pro", "Palatino Linotype", serif;
    --rounded: "Varela Round", "Arial Rounded MT Bold", sans-serif;
  }
  * { margin: 0; padding: 0; box-sizing: border-box; }
  html, body { width: 1200px; height: 675px; overflow: hidden; background: var(--page); }
  .canvas { position: relative; width: 1200px; height: 675px; }

  .card {
    position: absolute; top: 176px; width: 567px; height: 324px; overflow: hidden;
    background:
      repeating-linear-gradient(60deg, rgba(255,255,255,.05) 0 2px, transparent 2px 6px),
      repeating-linear-gradient(-60deg, rgba(0,0,0,.04) 0 2px, transparent 2px 6px),
      var(--card-grey);
  }
  .card--front { left: 29px; box-shadow: 4px 4px 0 #cfcfcf; }
  .card--back { left: 604px; border: 1px solid #333; }

  .band { position: absolute; left: 0; width: 100%; background: var(--band-green); }
  .card--front .band { top: 124px; height: 77px; }
  .band__panel { position: absolute; top: 0; height: 100%; background: var(--band-green-soft); }
  .band__panel--left { left: 0; width: 206px; }
  .band__panel--right { left: 360px; width: 207px; }
  .band__gap {
    position: absolute; left: 206px; width: 154px; top: 0; height: 100%;
    background: var(--card-grey);
  }

  .brand-name {
    position: absolute; top: 38px; left: 0; width: 100%; text-align: center;
    font-family: var(--rounded); font-weight: 400; font-size: 40px; letter-spacing: 3px;
    text-transform: uppercase; color: var(--brand-red);
  }
  .brand-mark {
    position: absolute; border-radius: 50%;
    background: radial-gradient(circle, #ffffff 0%, #f2f2f2 40%, rgba(255,255,255,0) 72%);
  }
  .card--front .brand-mark { left: 213px; top: 92px; width: 140px; height: 140px; }
  .card--back .brand-mark { left: 218px; top: 10px; width: 130px; height: 130px; }

  .contact-name {
    position: absolute; left: 0; width: 206px; top: 134px; text-align: center;
    font-family: var(--serif); font-weight: 700; font-size: 25px; color: var(--ink-magenta);
    text-shadow: 0 0 2px #fff, 0 0 2px #fff;
  }
  .contact-phone {
    position: absolute; left: 0; width: 206px; top: 166px; text-align: center;
    font-family: var(--serif); font-weight: 700; font-size: 19px; color: var(--ink-white);
  }
  .contact-email {
    position: absolute; left: 360px; width: 207px; top: 151px; text-align: center;
    font-family: var(--serif); font-weight: 700; font-size: 16px; color: var(--ink-magenta);
    text-shadow: 0 0 2px #fff, 0 0 2px #fff;
  }
  .tagline {
    position: absolute; left: 0; width: 100%; top: 226px; text-align: center;
    font-family: var(--serif); font-weight: 700; font-size: 21px; line-height: 28px; color: var(--ink-purple);
  }

  .card--back .band {
    top: 124px; height: 178px;
    background: linear-gradient(90deg, var(--band-green) 0%, var(--band-green-soft) 30%, var(--band-green-soft) 70%, var(--band-green) 100%);
  }
  .services { position: absolute; left: 97px; top: 140px; list-style: none; }
  .services__item {
    display: flex; align-items: center; height: 34px;
    font-family: var(--rounded); font-size: 17.5px;
    text-shadow: -1px 0 #fff, 1px 0 #fff, 0 -1px #fff, 0 1px #fff;
  }
  .services__item:last-child { height: 30px; }
  .services__flag { width: 22px; height: 10px; margin-right: 14px; flex: none; }
  .services__item--blue { color: var(--item-blue); }
  .services__item--red { color: var(--item-red); }
  .services__item--yellow { color: var(--item-yellow); }
  .services__item--green { color: var(--item-green); }
  .services__item--pink { color: var(--item-pink); }
</style>
</head>
<body>
<main class="canvas">
  <section class="card card--front">
    <h1 class="brand-name">Hopscotch Nell</h1>
    <div class="band">
      <div class="band__panel band__panel--left"></div>
      <div class="band__gap"></div>
      <div class="band__panel band__panel--right"></div>
    </div>
    <div class="brand-mark" role="img" aria-label="Hopscotch Nell brand mark area"></div>
    <p class="contact-name">Nellie Brannigan</p>
    <p class="contact-phone">583-402-9176</p>
    <p class="contact-email">nellie@hopscotchnell.biz</p>
    <p class="tagline">Personal Concierge and Errand Service<br>“Your errands done, your weekends back!”</p>
  </section>

  <section class="card card--back">
    <div class="band"></div>
    <div class="brand-mark" role="img" aria-label="Hopscotch Nell brand mark area"></div>
    <ul class="services">
      <li class="services__item services__item--blue"><svg class="services__flag" viewBox="0 0 22 10"><polygon points="0,1 22,0 4,10" fill="currentColor"/></svg>Personal Shopping and Errands</li>
      <li class="services__item services__item--red"><svg class="services__flag" viewBox="0 0 22 10"><polygon points="0,1 22,0 4,10" fill="currentColor"/></svg>Household Management</li>
      <li class="services__item services__item--yellow"><svg class="services__flag" viewBox="0 0 22 10"><polygon points="0,1 22,0 4,10" fill="currentColor"/></svg>Corporate Concierge</li>
      <li class="services__item services__item--green"><svg class="services__flag" viewBox="0 0 22 10"><polygon points="0,1 22,0 4,10" fill="currentColor"/></svg>Project Management</li>
      <li class="services__item services__item--pink"><svg class="services__flag" viewBox="0 0 22 10"><polygon points="0,1 22,0 4,10" fill="currentColor"/></svg>Group Rates for Teachers and Seniors</li>
    </ul>
  </section>
</main>
</body>
</html>
```